International freight forwarder experienced in perishable handling needs a web design

We need a website designed that will allow us to capture more customers through the website. We would like a visually appealing design that is not so heavy on text. Our business covers the logistics and freight forwarding industries and we have offices in South America and the USA. Our main customers are importers USA, Europe, Asia and Russia and we currently work almost exclusively with perishable products such as fresh cut flowers, fresh exotics fruits, cacao, fresh fish etc. We would like to convey a fresh, modern approach to freight forwarding focusing on concepts such as - time sensitive, anytime-anywhere delivery, innovation, experience, reliability and confidence. Should include links with Plumetta and Worvanet. Our core solutions include: Core Services
*Air Freight
*Ocean Freight
*Warehousing & Distribution
Our industry solutions cover
*Flowers
*FMCG including, fruits, vegetables
*Live animals
*Automotive
*Consumer Goods
*Industrial
*Oil & Gas
*Pharma
* Event logistics
* Project logistics

Target Market(s)

Importers in Europe, USA, Asia, Middle East and Russia

Number of Pages Required

4 page

Font styles to use
Sans Serif

Colors
a1cd39
606060
000000

Requirements
Must have
• Photos of fresh cut flowers, FMCG such as cacao, fresh fish (packaged for shipping), fresh exotic fruits, pharma products (packaged for shipping), oil and gas etc. Internal customer login access
Nice to have
• Photos of cargo shipping carriers and cargo airline carriers. Features similar to those of following website http://www.brolvacargo.com/eng/main/index.jsp?FromURL=web
Should not have
• Too much text, needs to be visually pleasing

```html
<!DOCTYPE html>
<html lang="en">
<head>
<meta charset="utf-8">
<title>Tranzora Alliance</title>
<link href="https://fonts.googleapis.com/css2?family=Oswald:wght@400;500&family=Lato:ital,wght@0,400;0,700;1,400&family=Roboto:wght@500;700&display=swap" rel="stylesheet">
<style>
:root{
  --green:#a1cd39;
  --green-dark:#7fa92a;
  --grey:#606060;
  --ink:#222;
  --light:#f0f0f0;
  --panel:#ececec;
  --footer:#343434;
  --footer-bar:#3e3e3e;
  --rule:#cfcfcf;
}
*{box-sizing:border-box;margin:0;padding:0}
html,body{width:877px;height:1200px;overflow:hidden}
body{position:relative;font-family:'Lato',sans-serif;color:var(--grey);background:#fff}
.abs{position:absolute}

/* header */
.site-header{left:0;top:0;width:877px;height:79px;background:linear-gradient(#fff,#f2f2f2)}
.brand{left:98px;top:38px;display:flex;align-items:center;gap:6px}
.brand-dot{width:14px;height:14px;border-radius:50%;background:var(--green)}
.brand-name{font:700 17px 'Lato',sans-serif;color:#444;letter-spacing:-.2px}
.socials{left:665px;top:11px;display:flex;gap:8px}
.socials span{width:24px;height:24px;border-radius:50%;border:2px solid var(--green);background:#fff}
.header-mail{left:645px;top:48px;font-size:10px;color:#444;display:flex;align-items:center;gap:6px}

/* nav */
.main-nav{left:0;top:79px;width:877px;height:35px;background:linear-gradient(#3a3a3a,#111);}
.main-nav a{position:absolute;top:12px;font:700 10.5px 'Roboto',sans-serif;color:#fff;text-decoration:none}
.main-nav .active{left:97px;top:8px;width:49px;height:19px;background:var(--green);text-align:center;line-height:19px;border:1px solid #c6e57a}
.nav-sep{position:absolute;top:8px;width:1px;height:19px;background:#555}
.nav-slash{left:640px;top:76px}
.nav-call{left:676px;top:92px;font:500 10px 'Roboto',sans-serif;color:#fff}

/* hero */
.hero{left:0;top:114px;width:877px;height:342px;background:linear-gradient(120deg,#5b4a46 0%,#7b3f5a 30%,#8c6a3a 55%,#4a4f5a 80%,#3b3b3f 100%)}
.hero-line1{left:102px;top:153px;font:italic 400 23px 'Lato',sans-serif;color:#fff;letter-spacing:.5px}
.hero-rule1{left:104px;top:184px;width:248px;height:1px;background:#fff}
.hero-line2{left:185px;top:184px;font:700 25px 'Lato',sans-serif;color:var(--green);letter-spacing:.5px}
.hero-rule2{left:192px;top:215px;width:250px;height:1px;background:#fff}
.hero-line3{left:412px;top:216px;font:italic 400 18px 'Lato',sans-serif;color:#fff}
.slide-arrow{top:156px;width:38px;height:35px;background:#4a4a4a;border:2px solid #8a8a8a;display:flex;align-items:center;justify-content:center}
.hero-dots{left:403px;top:319px;display:flex;gap:6px}
.hero-dots span{width:12px;height:12px;background:#fff}
.hero-dots .on{background:var(--green)}

/* welcome */
.welcome{left:0;top:456px;width:877px;height:231px;background:var(--light)}
.sec-title{font:400 17px 'Oswald',sans-serif;color:var(--ink);display:flex;align-items:center;gap:8px}
.sec-title em{font-style:normal;color:var(--green)}
.sec-rule{height:1px;background:var(--rule)}
.sec-rule::before{content:"";position:absolute;left:-12px;top:-3px;width:6px;height:6px;border:1px solid var(--rule)}
.welcome-brand{font:700 17px 'Lato',sans-serif;color:#444}
.welcome-text{left:98px;top:54px;width:382px;font-size:9.4px;line-height:13.4px;color:#444}
.welcome-text p+p{margin-top:5px}
.btn{left:97px;top:188px;width:62px;height:20px;background:var(--green);border:1px solid var(--green-dark);color:#fff;font:700 9px 'Lato',sans-serif;text-align:center;line-height:18px}
.video{left:507px;top:57px;width:274px;height:148px;background:linear-gradient(160deg,#1b4fa6,#3f8ee0 55%,#a9d4f5);box-shadow:0 6px 8px rgba(0,0,0,.25)}
.video-bar{left:0;bottom:0;width:274px;height:16px;background:#1a1a1a}
.video-progress{left:27px;top:7px;width:142px;height:3px;background:#d82020}
.video-track{left:169px;top:7px;width:28px;height:3px;background:#555}
.play{left:117px;top:59px;width:48px;height:30px;background:var(--green);border-radius:5px;opacity:.9}

/* industry */
.industry{left:0;top:687px;width:877px;height:201px;background:#fff}
.solution{top:65px;width:170px}
.sol-icon{width:57px;height:57px;border-radius:50%;background:radial-gradient(circle at 40% 35%,#b4db55,#86b424);box-shadow:0 3px 3px rgba(0,0,0,.2)}
.sol-name{left:69px;top:5px;font:500 12px 'Oswald',sans-serif;color:#222}
.sol-sub{left:69px;top:24px;font-size:9.5px;color:#777;white-space:nowrap}
.sol-desc{left:0;top:75px;width:160px;font-size:9.4px;line-height:13.4px;color:#444;word-break:break-all}
.car-arrow{top:100px}

/* review */
.review{left:0;top:888px;width:877px;height:144px;background:var(--panel)}
.avatar{left:113px;top:52px;width:63px;height:63px;border-radius:50%;border:2px solid var(--green);background:linear-gradient(#c8c2b8,#6b5a45)}
.quote{left:205px;top:57px;width:555px;font:italic 400 8.2px 'Lato',sans-serif;line-height:15.5px;color:#666}
.quote-mark{font:700 24px 'Lato',sans-serif;color:#c8c8c8;line-height:0;vertical-align:-6px}
.reviewer{left:209px;top:118px;font:700 9.5px 'Lato',sans-serif;color:#333;letter-spacing:.3px}
.review-dots{left:708px;top:125px;display:flex;gap:4px}
.review-dots span{width:7px;height:7px;border-radius:50%;background:#ccc}
.review-dots .on{background:var(--green)}

/* footer */
.site-footer{left:0;top:1032px;width:877px;height:143px;background:var(--footer)}
.f-col{top:18px}
.f-head{font:400 13.5px 'Oswald',sans-serif;color:#fff;padding-bottom:3px;border-bottom:1px solid #555}
.f-links{list-style:none;margin-top:6px}
.f-links li{font-size:9.5px;color:#ddd;line-height:18.3px;padding-left:11px;position:relative}
.f-links li::before{content:"›";position:absolute;left:0;color:#999}
.f-info{font-size:9.5px;color:#fff;line-height:13px;padding-left:20px;position:relative;margin-top:8px}
.f-info svg{position:absolute;left:0;top:0}
.map{left:0;top:27px;width:149px;height:85px;border:3px solid #fff;background:linear-gradient(135deg,#e8e4dc,#d9d4c8)}
.f-social{display:flex;gap:11px;margin-top:10px;padding-left:5px}
.f-social span{width:17px;height:17px;border-radius:50%;background:#ddd}
.f-brand{margin-top:16px;padding-left:14px;font:700 14px 'Lato',sans-serif;color:#ddd}
.footer-bar{left:0;top:1175px;width:877px;height:25px;background:var(--footer-bar);font-size:9.5px;color:#fff}
</style>
</head>
<body>

<header class="site-header abs">
  <div class="brand abs"><span class="brand-dot"></span><span class="brand-name">Tranzora Alliance</span></div>
  <div class="socials abs" aria-label="Social links"><span></span><span></span><span></span><span></span></div>
  <div class="header-mail abs">
    <svg width="12" height="9" viewBox="0 0 12 9"><rect x=".5" y=".5" width="11" height="8" fill="none" stroke="#666"/><path d="M.5 .5 6 5l5.5-4.5" fill="none" stroke="#666"/></svg>
    info@tranzoraalliance.com
  </div>
</header>

<nav class="main-nav abs">
  <a class="active">HOME</a>
  <span class="nav-sep" style="left:173px"></span>
  <a style="left:198px">About Us</a>
  <span class="nav-sep" style="left:273px"></span>
  <a style="left:304px">Core Services</a>
  <span class="nav-sep" style="left:404px"></span>
  <a style="left:435px">Our Network</a>
  <span class="nav-sep" style="left:528px"></span>
  <a style="left:558px">CONTACT US</a>
</nav>
<svg class="nav-slash abs" width="42" height="42" viewBox="0 0 42 42"><polygon points="30,0 40,0 12,42 2,42" fill="var(--green)"/></svg>
<div class="nav-call abs">CALL : 1800 5550 1472</div>

<section class="hero abs" role="img" aria-label="Warehouse worker securing a pallet of boxed fresh-cut flowers with netting">
  <div class="hero-line1 abs">We have experienced in</div>
  <div class="hero-rule1 abs"></div>
  <div class="hero-line2 abs">PERISHABLE GOODS</div>
  <div class="hero-rule2 abs"></div>
  <div class="hero-line3 abs">Handling</div>
  <div class="slide-arrow abs" style="left:10px"><svg width="10" height="14"><path d="M8 1 2 7l6 6" fill="none" stroke="#fff" stroke-width="2.5"/></svg></div>
  <div class="slide-arrow abs" style="left:829px"><svg width="10" height="14"><path d="M2 1l6 6-6 6" fill="none" stroke="#fff" stroke-width="2.5"/></svg></div>
  <div class="hero-dots abs"><span></span><span class="on"></span><span></span><span></span></div>
</section>

<section class="welcome abs">
  <h2 class="sec-title abs" style="left:98px;top:22px">Welcome To <span class="welcome-brand">Tranzora Alliance</span></h2>
  <div class="sec-rule abs" style="left:332px;top:34px;width:449px"></div>
  <div class="welcome-text abs">
    <p>Lorem ipsum dolor sit amet, consectetur adipiscing elit. Integer ut orci turpis. Nam volutpat, quam eu auctor dignissim, augue lacus luctus nunc, sit amet volutpat augue arcu nec lorem. Maecenas porttitor neque non neque feugiat suscipit. Phasellus orci risus, eleifend id venenatis sed, ultricies sed leo. Suspendisse semper, nunc sed pulvinar tempus, nulla orci ornare est, non vulputate lacus augue blandit lectus.</p>
    <p>Maecenas quis tortor faucibus, tempus metus eu, dictum libero. Morbi pharetra nisi id magna tincidunt sollicitudin. Curabitur porta, ligula et venenatis mattis, augue magna vestibulum ante, eu rutrum sapien arcu ac arcu. Sed at blandit nisl, sit amet pellentesque ligula. Fusce condimentum nisi justo, et interdum turpis sodales sed.</p>
  </div>
  <div class="btn abs">Read More</div>
  <div class="video abs" role="img" aria-label="Video still of a cargo plane over a world map and city port">
    <div class="play abs"><svg width="48" height="30"><polygon points="20,8 31,15 20,22" fill="#fff"/></svg></div>
    <div class="video-bar abs">
      <svg class="abs" style="left:12px;top:4px" width="6" height="8"><rect width="2" height="8" fill="#fff"/><rect x="4" width="2" height="8" fill="#fff"/></svg>
      <div class="video-progress abs"></div>
      <div class="video-track abs"></div>
      <div class="abs" style="left:142px;top:4px;width:8px;height:8px;border-radius:50%;background:#fff"></div>
      <div class="abs" style="left:230px;top:3px;width:34px;height:10px;border-radius:5px;background:#333"></div>
      <div class="abs" style="left:230px;top:2px;width:12px;height:12px;border-radius:50%;background:#eee"></div>
    </div>
  </div>
</section>

<section class="industry abs">
  <h2 class="sec-title abs" style="left:97px;top:26px">Our <em>Industry Solutions</em></h2>
  <div class="sec-rule abs" style="left:264px;top:38px;width:516px"></div>
  <svg class="car-arrow abs" style="left:54px" width="14" height="22"><path d="M12 2 3 11l9 9" fill="none" stroke="#333" stroke-width="3"/></svg>
  <svg class="car-arrow abs" style="left:808px" width="14" height="22"><path d="M2 2l9 9-9 9" fill="none" stroke="#333" stroke-width="3"/></svg>

  <div class="solution abs" style="left:97px">
    <div class="sol-icon abs" role="img" aria-label="Flower icon"></div>
    <div class="sol-name abs">Flowers</div><div class="sol-sub abs">ipsumdolo rsitamet</div>
    <div class="sol-desc abs">Loremipsumdolorsitamet,consectet uradipiscingelit.Morbifringillatincid unt risus nec vestibulum</div>
  </div>
  <div class="solution abs" style="left:273px">
    <div class="sol-icon abs" role="img" aria-label="Fruit icon"></div>
    <div class="sol-name abs">FMCG</div><div class="sol-sub abs">ipsum dolorsitamet</div>
    <div class="sol-desc abs">Loremipsumdolorsitamet,consectet uradipiscingelit.Morbifringillatincid unt risus nec vestibulum</div>
  </div>
  <div class="solution abs" style="left:449px">
    <div class="sol-icon abs" role="img" aria-label="Animal icon"></div>
    <div class="sol-name abs">Live Animals</div><div class="sol-sub abs">ipsumdo lorsitamet</div>
    <div class="sol-desc abs">Loremipsumdolorsitamet,consectet uradipiscingelit.Morbifringillatincid unt risus nec vestibulum</div>
  </div>
  <div class="solution abs" style="left:626px">
    <div class="sol-icon abs"><svg width="57" height="57"><rect x="21" y="28" width="9" height="9" fill="#fff"/><rect x="30" y="28" width="7" height="9" fill="#fff" opacity=".8"/><rect x="26" y="20" width="9" height="8" fill="#fff" opacity=".9"/></svg></div>
    <div class="sol-name abs">Consumer Goods</div><div class="sol-sub abs">Cras sit amet isa fer.</div>
    <div class="sol-desc abs">Loremipsumdolorsitamet,consectet uradipiscingelit.Morbifringillatincid unt risus nec vestibulum</div>
  </div>
</section>

<section class="review abs">
  <h2 class="sec-title abs" style="left:97px;top:10px">Our <em>Customers Review</em></h2>
  <div class="sec-rule abs" style="left:264px;top:22px;width:516px"></div>
  <div class="avatar abs" role="img" aria-label="Customer portrait"></div>
  <p class="quote abs"><span class="quote-mark">“</span> Lorem ipsum dolor sit amet consectetur adipisicing elitsed do eiusmod tempor incididunt ut labore et dolore magna aliqua. Ut enim ad minim vesniam, quis nostrud exercitation ullamco laboris nisi ut aliquip ex ea commodo consequat. Duis aute irure dolor in reprehenderit in voluptate velit esse cillum is a dolore eu fugiat nulla pariatur. Excepteur sint occaecat cupidatat non proident, sunt in culpa qui officia deserunt mollit <span class="quote-mark">”</span></p>
  <div class="reviewer abs">Mr. Dorian Vell</div>
  <div class="review-dots abs"><span class="on"></span><span></span><span></span><span></span></div>
</section>

<footer class="site-footer abs">
  <div class="f-col abs" style="left:98px;width:122px">
    <h3 class="f-head">Quick Links</h3>
    <ul class="f-links"><li>Home</li><li>About Us</li><li>Core Services</li><li>Our Network</li><li>Contact Us</li></ul>
  </div>
  <div class="f-col abs" style="left:271px;width:123px">
    <h3 class="f-head">Contact Info</h3>
    <div class="f-info"><svg width="10" height="14"><path d="M5 0a5 5 0 0 1 5 5c0 4-5 9-5 9S0 9 0 5a5 5 0 0 1 5-5z" fill="#999"/><circle cx="5" cy="5" r="2" fill="#343434"/></svg>16 Nemo enim ipsam vuptat voluptas spe ut odit</div>
    <div class="f-info" style="margin-top:10px"><svg width="11" height="11"><path d="M2 0 4 0 5 3 3.5 4.5a7 7 0 0 0 3 3L8 6l3 1v2c0 1-1 2-2 2A9 9 0 0 1 0 2c0-1 1-2 2-2z" fill="#999"/></svg>555-014-2290</div>
    <div class="f-info" style="margin-top:9px"><svg width="11" height="9"><rect x=".5" y=".5" width="10" height="8" fill="none" stroke="#999"/><path d="M.5 .5 5.5 5l5-4.5" fill="none" stroke="#999"/></svg>info@tranzoraalliance.com</div>
  </div>
  <div class="abs" style="left:417px;top:20px;width:1px;height:110px;background:#444"></div>
  <div class="f-col abs" style="left:446px;width:150px">
    <h3 class="f-head">View Location</h3>
    <div class="map abs" role="img" aria-label="Street map showing office location"></div>
  </div>
  <div class="abs" style="left:622px;top:20px;width:1px;height:110px;background:#444"></div>
  <div class="f-col abs" style="left:647px;width:134px">
    <h3 class="f-head">Connect</h3>
    <div class="f-social" aria-label="Social links"><span></span><span></span><span></span><span></span></div>
    <div class="f-brand">Tranzora Alliance</div>
  </div>
</footer>
<div class="footer-bar abs">
  <span class="abs" style="left:97px;top:7px">Copyright © 2015 Tranzora Alliance</span>
  <span class="abs" style="left:632px;top:7px">Sitemap &nbsp;::&nbsp; Privacy &nbsp;::&nbsp; Contact Us</span>
</div>

</body>
</html>
```